National hospice pharmacy network needs a powerpoint design

We need a power point design for a new company that is creating a network of independent pharmacies to provide medication delivery to hospice patients in their area. We will be providing them with logistics to build a delivery system, software to increase efficiency and the marketing to hospice agencies. The pharmacies will benefit with increasing their patient care, increasing their efficiency and increasing their profits.

Pharmacy

```html
<!DOCTYPE html>
<html lang="en">
<head>
<meta charset="utf-8">
<title>HospiRoute – Pharmacy Network Presentation</title>
<link rel="stylesheet" href="https://fonts.googleapis.com/css2?family=Open+Sans:wght@300;400;600;700&display=swap">
<style>
  :root{
    --canvas:#c0c3c6;
    --slide-bg:#eef2f7;
    --white:#ffffff;
    --navy:#23508e;
    --brand-blue:#2a5a9a;
    --green:#4cb84f;
    --text:#1f4b86;
    --circle-green:#5dbb63;
    --circle-teal:#4fbdb5;
    --circle-blue:#4a73ad;
    --rule:#e1e6ee;
  }
  *{box-sizing:border-box;margin:0;padding:0}
  html,body{width:1064px;height:1200px;overflow:hidden;background:var(--canvas)}
  body{font-family:"Open Sans",Arial,sans-serif;position:relative}
  .slide{position:absolute;width:516px;height:386px;background:var(--slide-bg);overflow:hidden}
  .col-a{left:12px}.col-b{left:536px}
  .row-1{top:9px}.row-2{top:406px}.row-3{top:805px;height:387px}

  .slide-title{position:absolute;left:0;top:0;width:100%;height:37px;background:var(--white);
    border-bottom:1px solid var(--rule);color:var(--navy);font-size:26px;font-weight:400;text-align:center;line-height:40px;white-space:nowrap}

  .slide-footer{position:absolute;left:0;bottom:0;width:100%;height:33px;background:var(--brand-blue);
    display:flex;align-items:center;padding:0 10px 0 9px;color:var(--white);white-space:nowrap}
  .footer-brand{font-size:15px;letter-spacing:-.4px}
  .footer-tagline{font-size:7.5px;margin-left:7px}
  .footer-url{margin-left:auto;font-size:7.5px;color:var(--green)}
  .footer-page{font-size:7.5px;margin-left:18px}

  /* title slide */
  .cover-brand{position:absolute;left:0;width:100%;top:128px;text-align:center;color:var(--brand-blue);
    font-size:74px;font-weight:700;letter-spacing:-3px;line-height:1}
  .cover-tagline{position:absolute;left:0;width:100%;padding-left:150px;top:227px;text-align:center;color:var(--brand-blue);font-size:14.5px}

  /* bullet lists */
  .point-list{position:absolute;left:72px;top:68px;list-style:none}
  .point{margin-bottom:6px}
  .point-head{font-size:18px;font-weight:600;color:var(--text);display:flex;align-items:center;gap:4px;margin-left:-23px;line-height:26px}
  .point-head svg{width:19px;height:19px}
  .sub-list{list-style:none;margin-left:10px}
  .sub-item{font-size:13px;color:var(--text);line-height:26px;position:relative;padding-left:13px}
  .sub-item::before{content:"";position:absolute;left:0;top:10px;border-left:5px solid var(--green);
    border-top:3.5px solid transparent;border-bottom:3.5px solid transparent}
  .sub-item.wrap{max-width:390px}

  .check-list{position:absolute;top:108px;list-style:none}
  .check-group{margin-bottom:8px}
  .check-head{font-size:18px;font-weight:600;color:var(--text);line-height:25px}
  .check-item{font-size:13.5px;color:var(--text);line-height:22px;padding-left:8px;white-space:nowrap}
  .check-item .tick{color:var(--green);margin-right:5px}
  .profits .check-list{left:72px}
  .care .check-list{left:45px}

  /* process slide */
  .steps{position:absolute;left:0;top:37px;width:516px;height:316px}
  .step-caption{position:absolute;width:100px;text-align:center;color:var(--white);font-size:11px;line-height:15px}
  .step-number{position:absolute;width:100px;text-align:center;color:var(--white);font-size:64px;font-weight:300;line-height:1}
  .delivery-note{position:absolute;left:0;width:100%;top:307px;text-align:center;color:var(--green);font-size:14px}

  /* closing slide */
  .closing{background:var(--brand-blue)}
  .closing-brand{position:absolute;left:0;width:100%;top:128px;text-align:center;color:var(--white);
    font-size:54px;font-weight:700;letter-spacing:-2px;line-height:1}
  .closing-line{position:absolute;left:0;width:100%;top:208px;text-align:center;color:var(--white);font-size:38px;font-weight:400;white-space:nowrap}
  .closing-line .amp{color:var(--green)}
</style>
</head>
<body>

<section class="slide col-a row-1 cover">
  <div class="cover-brand">HospiRoute</div>
  <div class="cover-tagline">Bringing Care Closer to Home</div>
</section>

<section class="slide col-b row-1 efficiencies">
  <h2 class="slide-title">Increased Efficiencies</h2>
  <ul class="point-list">
    <li class="point">
      <div class="point-head"><svg viewBox="0 0 20 20"><circle cx="10" cy="10" r="8.5" fill="none" stroke="#4fbdb5" stroke-width="1.4"/><line x1="4" y1="16" x2="16" y2="4" stroke="#4fbdb5" stroke-width="1.4"/></svg>No Data Entry</div>
      <ul class="sub-list">
        <li class="sub-item wrap">Software that seamlessly communicates between prescribers and your pharmacy</li>
        <li class="sub-item">Essentially the hospice&nbsp; does all the data entry</li>
      </ul>
    </li>
    <li class="point">
      <div class="point-head"><svg viewBox="0 0 20 20"><circle cx="10" cy="10" r="8.5" fill="none" stroke="#4fbdb5" stroke-width="1.4"/><line x1="4" y1="16" x2="16" y2="4" stroke="#4fbdb5" stroke-width="1.4"/></svg>No Phone Calls</div>
      <ul class="sub-list">
        <li class="sub-item">All scripts new and refill done electronically</li>
        <li class="sub-item">Clinical consultation done by contracted pharmacists</li>
      </ul>
    </li>
    <li class="point">
      <div class="point-head"><svg viewBox="0 0 20 20"><circle cx="10" cy="10" r="8.5" fill="none" stroke="#4fbdb5" stroke-width="1.4"/><line x1="4" y1="16" x2="16" y2="4" stroke="#4fbdb5" stroke-width="1.4"/></svg>No Third Party Billing</div>
      <ul class="sub-list">
        <li class="sub-item">Billing and Medicare reporting done for you</li>
      </ul>
    </li>
  </ul>
  <footer class="slide-footer"><span class="footer-brand">HospiRoute</span><span class="footer-tagline">| &nbsp;Bringing Care Closer to Home</span><span class="footer-url">www.hospiroute.com</span><span class="footer-page">3</span></footer>
</section>

<section class="slide col-a row-2 process">
  <h2 class="slide-title">Easy as 1,2,3…..delivered</h2>
  <div class="steps">
    <svg width="516" height="316" viewBox="0 0 516 316">
      <circle cx="113" cy="143" r="90" fill="var(--circle-green)" opacity=".85"/>
      <circle cx="258" cy="143" r="90" fill="var(--circle-teal)" opacity=".8"/>
      <circle cx="402" cy="143" r="90" fill="var(--circle-blue)" opacity=".82"/>
    </svg>
    <div class="step-number" style="left:63px;top:104px">1</div>
    <div class="step-number" style="left:208px;top:104px">2</div>
    <div class="step-number" style="left:352px;top:104px">3</div>
    <div class="step-caption" style="left:63px;top:182px">Order entered by hospice.</div>
    <div class="step-caption" style="left:212px;top:170px">Prescription sent to prescriber for signature.</div>
    <div class="step-caption" style="left:358px;top:174px">Prescription sent to pharmacy for filling.</div>
  </div>
  <div class="delivery-note">Pharmacy delivers prescription.</div>
  <footer class="slide-footer"><span class="footer-brand">HospiRoute</span><span class="footer-tagline">| &nbsp;Bringing Care Closer to Home</span><span class="footer-url">www.hospiroute.com</span><span class="footer-page">4</span></footer>
</section>

<section class="slide col-b row-2 profits">
  <h2 class="slide-title">Increased Profits</h2>
  <ul class="check-list">
    <li class="check-group"><div class="check-head">Script Volume</div><div class="check-item"><span class="tick">✓</span>Hospice prescriptions in you area routed to your pharmacy</div></li>
    <li class="check-group"><div class="check-head">Marketing</div><div class="check-item"><span class="tick">✓</span>We contract with hospices on your behalf</div></li>
    <li class="check-group"><div class="check-head">Delivery</div><div class="check-item"><span class="tick">✓</span>You are paid $10 per delivery</div></li>
  </ul>
  <footer class="slide-footer"><span class="footer-brand">HospiRoute</span><span class="footer-tagline">| &nbsp;Bringing Care Closer to Home</span><span class="footer-url">www.hospiroute.com</span><span class="footer-page">5</span></footer>
</section>

<section class="slide col-a row-3 care">
  <h2 class="slide-title">Increased Patient Care</h2>
  <ul class="check-list">
    <li class="check-group"><div class="check-head">Local</div><div class="check-item"><span class="tick">✓</span>Many hospice patients are forced to use mail order</div></li>
    <li class="check-group"><div class="check-head">Fast Delivery</div><div class="check-item"><span class="tick">✓</span>Consistent same day delivery</div></li>
    <li class="check-group"><div class="check-head">Positive Impact</div><div class="check-item"><span class="tick">✓</span>Software is intuitive and easily fits around any pharmacy work flow</div></li>
  </ul>
  <footer class="slide-footer"><span class="footer-brand">HospiRoute</span><span class="footer-tagline">| &nbsp;Bringing Care Closer to Home</span><span class="footer-url">www.hospiroute.com</span><span class="footer-page">6</span></footer>
</section>

<section class="slide col-b row-3 closing">
  <div class="closing-brand">HospiRoute</div>
  <div class="closing-line">Questions <span class="amp">&amp;</span> Concerns</div>
</section>

</body>
</html>
```